Short term vacation rental

I need a simple site the we can rent a duplex that is on the sand in Indian rocks beach Fl needs to be able to sync with multiple calendars like staylumo.com qelt tovn using Wordpress

```html
<!DOCTYPE html>
<html lang="en">
<head>
<meta charset="UTF-8">
<title>Tidewater Haven · Indian Rocks Beach Duplex</title>
<link href="https://fonts.googleapis.com/css2?family=Inter:wght@400;500;600&family=Playfair+Display:ital,wght@0,600;0,700;1,600&display=swap" rel="stylesheet">
<style>
:root{
  --ocean:#0a6aa8;
  --ocean-deep:#0d5f8c;
  --teal:#0c6b74;
  --ink:#1d2a33;
  --text:#3f4a52;
  --muted:#5f6a72;
  --page:#f5f5f6;
  --band:#f1f1f3;
  --white:#ffffff;
  --sky:#9ae8f8;
  --sand:#e6e4cc;
  --icon-bg:#d8ecfd;
}
*{box-sizing:border-box;margin:0;padding:0}
html,body{width:1200px;height:2286px;overflow:hidden}
body{background:var(--page);font-family:"Inter",sans-serif;color:var(--text);position:relative}
.serif{font-family:"Playfair Display",serif}

/* Navigation */
.site-nav{position:absolute;top:0;left:0;width:1200px;height:51px;background:#f1eff0;display:flex;align-items:center;z-index:5}
.brand{position:absolute;left:213px;top:14px;display:flex;align-items:center;gap:6px;font-size:12px;font-weight:500;letter-spacing:.6px;color:var(--ocean-deep)}
.brand-dot{width:10px;height:10px;border-radius:50%;background:var(--ocean-deep)}
.nav-links{position:absolute;left:430px;top:16px;display:flex;gap:23px;font-size:12px;color:#39434a}
.nav-links .active{color:var(--ocean);border-bottom:2px solid var(--ocean);padding-bottom:4px}
.btn-book{position:absolute;left:906px;top:11px;width:89px;height:29px;border-radius:15px;background:var(--ocean);color:#fff;font-size:12px;font-weight:500;display:flex;align-items:center;justify-content:center}

/* Hero */
.hero{position:absolute;top:51px;left:0;width:1200px;height:598px}
.hero-photo{position:absolute;inset:0;background:linear-gradient(180deg,#8d8f9c 0%,#e98a55 15%,#f0a862 28%,#b6c0cc 42%,#2d6f9e 47%,#1f5a8a 62%,#6e8ea0 75%,#cbb691 82%,#d8cfc0 92%,#9fb0b8 100%)}
.hero-copy{position:absolute;left:205px;top:172px;width:470px;color:#fff}
.hero-copy h1{font-size:36px;line-height:43px;font-weight:700}
.hero-copy p{margin-top:18px;font-size:13px;line-height:20.5px}
.hero-actions{position:absolute;left:205px;top:335px;display:flex;gap:11px}
.btn{height:41px;border-radius:5px;font-size:12px;font-weight:500;display:flex;align-items:center;justify-content:center;color:#fff}
.btn-primary{width:139px;background:var(--ocean)}
.btn-ghost{width:103px;background:rgba(255,255,255,.28);border:1px solid rgba(255,255,255,.45)}
.scroll-cue{position:absolute;left:592px;top:544px}

/* Haven */
.haven{position:absolute;top:649px;left:0;width:1200px;height:556px;background:var(--page)}
.haven-photo{position:absolute;left:205px;top:45px;width:372px;height:465px;border-radius:14px;background:linear-gradient(180deg,#dcd7d0 0%,#c9c2b6 12%,#a9c7d8 32%,#4c8fb2 45%,#c5b99c 55%,#8e8466 66%,#c9bfae 75%,#8a7a64 100%);box-shadow:0 16px 30px rgba(0,0,0,.14)}
.quote-card{position:absolute;left:374px;top:403px;width:226px;height:130px;background:#fff;border-radius:8px;padding:18px 18px;box-shadow:0 10px 26px rgba(0,0,0,.12)}
.quote-card .title{font-size:11px;color:var(--teal);font-style:italic}
.quote-card p{margin-top:6px;font-size:11px;line-height:17px;color:#4b545a}
.stars{margin-top:6px;font-size:10px;letter-spacing:3px;color:var(--teal)}
.haven-copy{position:absolute;left:622px;top:108px;width:370px}
.haven-copy h2{font-size:26px;color:var(--ocean-deep);font-weight:700}
.lead{margin-top:18px;font-size:13px;line-height:20.5px;color:#404a51}
.body{margin-top:16px;font-size:11.2px;line-height:18px;color:#4a545b}
.checks{list-style:none;margin-top:20px}
.checks li{display:flex;align-items:center;gap:11px;font-size:11.3px;color:#2d363c;margin-bottom:13px}
.link-more{margin-top:20px;display:flex;align-items:center;gap:8px;font-size:11.5px;color:var(--ocean-deep)}

/* Amenities */
.amenities{position:absolute;top:1205px;left:0;width:1200px;height:634px;background:var(--band)}
.amenities h2{position:absolute;top:45px;width:1200px;text-align:center;font-size:27px;color:var(--ink);font-weight:700}
.amenities .sub{position:absolute;top:88px;left:395px;width:410px;text-align:center;font-size:11.5px;line-height:17px;color:#4a545b}
.card{position:absolute;border-radius:14px}
.card-feature{left:205px;top:166px;width:386px;height:423px;background:linear-gradient(180deg,#2f8fd0 0%,#8cc6e6 40%,#2fa6a8 48%,#d6d0bf 58%,#7a6b58 75%,#3e342c 100%);overflow:hidden}
.feature-copy{position:absolute;left:23px;bottom:23px;width:340px;color:#fff}
.badge{display:inline-block;background:var(--teal);color:#fff;font-size:9px;padding:3px 8px;border-radius:9px}
.feature-copy h3{margin-top:9px;font-size:12px;font-weight:700}
.feature-copy p{margin-top:8px;font-size:11.2px;line-height:17px}
.card-kitchen{left:608px;top:166px;width:387px;height:203px;background:#fff;display:flex;align-items:center;padding:0 22px;gap:23px}
.icon-tile{width:45px;height:45px;border-radius:9px;background:var(--icon-bg);display:flex;align-items:center;justify-content:center;flex:none}
.card h3.serif{font-size:12px;font-weight:700;color:var(--ink)}
.card-kitchen p{margin-top:6px;font-size:11.2px;line-height:17px;color:#3b454c}
.card-small{top:387px;width:185px;height:202px;padding:26px 22px}
.card-sunset{left:608px;background:var(--sky)}
.card-wifi{left:810px;background:var(--sand)}
.card-small h3{margin-top:18px}
.card-sunset h3{color:#0a5f7a}
.card-sunset p{color:#0d6d84}
.card-wifi h3{color:#3d4a3e}
.card-wifi p{color:#5e6458}
.card-small p{margin-top:8px;font-size:11.2px;line-height:17px}

/* CTA */
.cta{position:absolute;top:1839px;left:0;width:1200px;height:309px;overflow:hidden}
.cta-photo{position:absolute;inset:0;background:linear-gradient(180deg,#1d5185 0%,#24608f 40%,#223f5c 62%,#34506a 78%,#5a4436 100%)}
.cta h2{position:absolute;top:44px;width:1200px;text-align:center;font-size:34px;color:#fff;font-weight:700}
.cta p{position:absolute;top:108px;left:330px;width:540px;text-align:center;font-size:13px;line-height:20.5px;color:#fff}
.booking-bar{position:absolute;left:340px;top:179px;width:519px;height:85px;border-radius:10px;background:rgba(255,255,255,.45);display:flex;align-items:center;gap:12px;padding:0 12px}
.field{width:107px;height:45px;border-radius:6px;background:rgba(255,255,255,.22);padding:6px 12px;font-size:11px;line-height:17px;color:rgba(255,255,255,.8)}
.field .value{color:rgba(255,255,255,.9);font-weight:500}
.field-guests{height:62px;padding-top:2px}
.btn-check{width:139px;height:39px;border-radius:5px;background:#fff;color:var(--ocean-deep);font-size:12px;font-weight:500;display:flex;align-items:center;justify-content:center}

/* Footer */
.site-footer{position:absolute;top:2148px;left:0;width:1200px;height:138px;background:var(--band)}
.footer-brand{position:absolute;left:205px;top:26px;display:flex;align-items:center;gap:7px;font-size:14px;font-weight:500;letter-spacing:.6px;color:var(--ocean-deep)}
.footer-brand .brand-dot{width:12px;height:12px}
.footer-tag{position:absolute;left:205px;top:72px;width:215px;font-size:11.3px;line-height:17px;color:#3b454c}
.footer-links{position:absolute;left:448px;top:66px;display:flex;gap:23px;font-size:8.6px;color:#3b454c}
.footer-links .copy{margin-left:-6px;color:#5a646b}
</style>
</head>
<body>

<header class="site-nav">
  <div class="brand"><span class="brand-dot"></span>TIDEWATER HAVEN</div>
  <nav class="nav-links">
    <span class="active">The Property</span><span>Amenities</span><span>Availability</span><span>Reviews</span><span>Location</span>
  </nav>
  <div class="btn-book">Book Now</div>
</header>

<section class="hero">
  <div class="hero-photo" role="img" aria-label="Sunset over the Gulf with dunes and beach grass"></div>
  <div class="hero-copy">
    <h1 class="serif">Experience Coastal Serenity at Indian Rocks Beach</h1>
    <p>Luxury duplex living meets the rhythmic waves of the Gulf. Your private sanctuary for sunsets, sand, and soul-refreshing retreats.</p>
  </div>
  <div class="hero-actions">
    <div class="btn btn-primary">Check Availability</div>
    <div class="btn btn-ghost">View Units</div>
  </div>
  <svg class="scroll-cue" width="16" height="16" viewBox="0 0 16 16" fill="none" stroke="#fff" stroke-width="2"><path d="M3 3l5 5 5-5M3 8l5 5 5-5"/></svg>
</section>

<section class="haven">
  <div class="haven-photo" role="img" aria-label="Bright living room with floor-to-ceiling windows facing the beach"></div>
  <div class="quote-card">
    <div class="title serif">"Pure Bliss"</div>
    <p>"The most relaxing stay we've ever had. Every window frames a postcard view."</p>
    <div class="stars">★★★★★</div>
  </div>
  <div class="haven-copy">
    <h2 class="serif">Your Private Beach Haven</h2>
    <p class="lead">Located directly on the powder-white sands of Indian Rocks Beach, our duplex offers two distinct, luxury-appointed units designed for the ultimate coastal lifestyle.</p>
    <p class="body">Whether you're booking one unit for a romantic escape or both for a family reunion, you'll find every detail curated for comfort—from high-thread-count linens to professional-grade kitchens and expansive private decks.</p>
    <ul class="checks">
      <li><svg width="15" height="15" viewBox="0 0 16 16" fill="none" stroke="#0c6b74" stroke-width="1.4"><circle cx="8" cy="8" r="6.5"/><path d="M5 8.2l2 2 4-4"/></svg>Two 3-Bedroom Units with En-suite Baths</li>
      <li><svg width="15" height="15" viewBox="0 0 16 16" fill="none" stroke="#0c6b74" stroke-width="1.4"><circle cx="8" cy="8" r="6.5"/><path d="M5 8.2l2 2 4-4"/></svg>Private Gulf-Front Balconies</li>
      <li><svg width="15" height="15" viewBox="0 0 16 16" fill="none" stroke="#0c6b74" stroke-width="1.4"><circle cx="8" cy="8" r="6.5"/><path d="M5 8.2l2 2 4-4"/></svg>Smart Home Technology Throughout</li>
    </ul>
    <div class="link-more">Explore the Interior <svg width="13" height="12" viewBox="0 0 13 12" fill="none" stroke="#0d5f8c" stroke-width="1.5"><path d="M1 6h10M7 2l4 4-4 4"/></svg></div>
  </div>
</section>

<section class="amenities">
  <h2 class="serif">Elevated Amenities</h2>
  <p class="sub">Everything you need for a seamless, luxurious seaside stay is right at your fingertips.</p>

  <div class="card card-feature" role="img" aria-label="Wooden boardwalk through sea oats leading to the beach">
    <div class="feature-copy">
      <span class="badge">Featured</span>
      <h3 class="serif">Direct Beach Access</h3>
      <p>Walk from your doorstep directly onto the sand. No roads to cross, just the ocean breeze.</p>
    </div>
  </div>

  <div class="card card-kitchen">
    <div class="icon-tile"><svg width="18" height="18" viewBox="0 0 18 18" fill="none" stroke="#0d5f8c" stroke-width="1.8" stroke-linecap="round"><path d="M4 2v5a2 2 0 0 0 4 0V2M6 2v14M13 2c-2 1-2 5-2 7h2v7"/></svg></div>
    <div>
      <h3 class="serif">Chef's Kitchen</h3>
      <p>Frostline appliances, quartz countertops, and a full suite of culinary tools.</p>
    </div>
  </div>

  <div class="card card-small card-sunset">
    <svg width="22" height="18" viewBox="0 0 22 18" fill="none" stroke="#0a5f7a" stroke-width="1.6" stroke-linecap="round"><path d="M6 12a5 5 0 0 1 10 0M2 15h18M11 2v3M4 6l2 2M18 6l-2 2"/></svg>
    <h3 class="serif">Sunset Views</h3>
    <p>Unobstructed westward views of the world-famous Florida sunsets.</p>
  </div>

  <div class="card card-small card-wifi">
    <svg width="22" height="18" viewBox="0 0 22 18" fill="none" stroke="#2f3a31" stroke-width="1.8" stroke-linecap="round"><path d="M2 6a13 13 0 0 1 18 0M5 9.5a8.5 8.5 0 0 1 12 0M8 13a4 4 0 0 1 6 0"/><circle cx="11" cy="16" r="1" fill="#2f3a31"/></svg>
    <h3 class="serif">Ultra-Fast WiFi</h3>
    <p>Seamless connectivity for those who need to stay productive from the beach.</p>
  </div>
</section>

<section class="cta">
  <div class="cta-photo" role="img" aria-label="Blurred view of the sea at dusk from a wooden deck railing"></div>
  <h2 class="serif">Ready for Your Escape?</h2>
  <p>Dates fill up quickly during the peak season. Secure your beachfront retreat today and start counting down to paradise.</p>
  <div class="booking-bar">
    <div class="field">Check In<br><span class="value">Select Date</span></div>
    <div class="field">Check Out<br><span class="value">Select Date</span></div>
    <div class="field field-guests">Guests<br><span class="value">2 Adults, 1 Child</span></div>
    <div class="btn-check">Check Availability</div>
  </div>
</section>

<footer class="site-footer">
  <div class="footer-brand"><span class="brand-dot"></span>TIDEWATER HAVEN</div>
  <p class="footer-tag">Luxury vacation rentals in Indian Rocks Beach. Where the sand meets the soul.</p>
  <div class="footer-links">
    <span>Privacy Policy</span><span>Terms of Service</span><span>Rental Agreement</span><span>Contact Us</span>
    <span class="copy">© 2024 Indian Rocks Beach Duplex. All rights reserved.</span>
  </div>
</footer>

</body>
</html>
```